Business Card Design

I would like a new business card for my business Drive Keystone, we operate within the automotive industry and offer customer retention solutions for independent mechanical workshops across Australia and New Zealand. The program incorporates service reminders and roadside assistance for consumers and is designed to get the client back for their vehicle service visit, I would like a doubled sided design that incorporates my logos and a two tone type card that has white and a carbon fibre look also use the blue in the logo I have uploaded. It would be great to have icons as the phone/fax/email etc details for the card are below. The finished design must be a print ready file useable.It would be great if the design could communicate the what type of business we are
Philip Marsh
General Manager
Drive Keystone Pty Ltd
Unit 5/42 Tolmer Street
Kelverton Newcastle NSW 2289
Ph:+61247318500
fax:+61247318600
Mobile:0412958364
Email:info@drivekeystone.com.au
Updates
I have just upload a carbon fibre background for the business card hope it helps
Hello guys I am sorry fr no feedback I have been away over seas I will send feedback when I return monday
Industry/Entity Type
Automotive
Look and feel
Each slider illustrates characteristics of the customer's brand and the style your logo design should communicate.

```html
<!DOCTYPE html>
<html lang="en">
<head>
<meta charset="utf-8">
<title>Drive Keystone – Business Card</title>
<link rel="stylesheet" href="https://fonts.googleapis.com/css2?family=Montserrat:wght@400;600&display=swap">
<style>
  :root {
    --stage: #2c2c2e;
    --card-white: #ffffff;
    --card-shade: #f1f2f4;
    --brand-blue: #3fc0f5;
    --brand-teal: #1aa9b8;
    --ink-dark: #2a2f37;
    --ink-light: #ffffff;
    --back-black: #050505;
  }
  * { box-sizing: border-box; margin: 0; padding: 0; }
  html, body {
    width: 1200px; height: 821px; overflow: hidden;
    background: var(--stage);
    font-family: "Montserrat", sans-serif;
  }
  .canvas { position: relative; width: 1200px; height: 821px; }

  .card {
    position: absolute; top: 100px;
    width: 440px; height: 620px;
    background: linear-gradient(135deg, var(--card-white) 0%, var(--card-shade) 100%);
    box-shadow: 0 18px 40px rgba(0,0,0,.55);
    overflow: hidden;
  }
  .card--front { left: 120px; }
  .card--back  { left: 640px; padding: 20px; }

  /* front */
  .info-panel {
    position: absolute; left: 170px; top: 14px;
    width: 256px; height: 466px;
    background: var(--brand-blue);
  }
  .divider {
    position: absolute; left: 168px; top: 0;
    width: 3px; height: 480px;
    background: var(--ink-dark);
  }
  .name-first {
    position: absolute; right: 282px; top: 64px;
    font-size: 30px; font-weight: 400; letter-spacing: 3px;
    color: var(--brand-teal);
  }
  .name-last {
    position: absolute; left: 182px; top: 64px;
    font-size: 30px; font-weight: 600; letter-spacing: 3px;
    color: var(--ink-dark);
  }
  .job-title {
    position: absolute; left: 184px; top: 104px;
    font-size: 13px; letter-spacing: 1.5px;
    color: var(--ink-dark);
  }
  .contact-list { list-style: none; }
  .contact-item {
    position: absolute; left: 140px;
    display: flex; align-items: flex-start;
  }
  .contact-icon {
    width: 28px; height: 28px; flex: none;
    background: var(--brand-blue);
    border: 2px solid var(--card-white);
    box-shadow: 0 1px 3px rgba(0,0,0,.35);
    display: flex; align-items: center; justify-content: center;
  }
  .contact-icon svg { width: 16px; height: 16px; fill: var(--ink-dark); }
  .contact-text {
    margin-left: 16px; padding-top: 4px;
    font-size: 15px; line-height: 24px; letter-spacing: .5px;
    color: var(--ink-light);
  }
  .contact-item--address { top: 190px; }
  .contact-item--phone   { top: 270px; }
  .contact-item--email   { top: 330px; }
  .contact-item--web     { top: 390px; }

  .brand {
    position: absolute; left: 10px; top: 300px; width: 124px;
    display: flex; flex-direction: column; align-items: center;
  }
  .brand-mark {
    width: 86px; height: 86px; border-radius: 50%;
    background: var(--brand-blue);
  }
  .brand-name {
    margin-top: 12px;
    font-size: 14px; font-weight: 600; letter-spacing: .5px;
    color: var(--brand-blue); text-align: center; white-space: nowrap;
  }

  /* back */
  .back-face { width: 100%; height: 100%; background: var(--back-black); }
</style>
</head>
<body>
<main class="canvas">
  <section class="card card--front" aria-label="Business card front">
    <div class="info-panel"></div>
    <div class="divider"></div>

    <p class="name-first">DANIEL</p>
    <p class="name-last">HORTON</p>
    <p class="job-title">FINANCIAL ADVISOR</p>

    <ul class="contact-list">
      <li class="contact-item contact-item--address">
        <span class="contact-icon"><svg viewBox="0 0 16 16" aria-hidden="true"><path d="M8 1a5 5 0 0 0-5 5c0 3.6 5 9 5 9s5-5.4 5-9a5 5 0 0 0-5-5zm0 7a2 2 0 1 1 0-4 2 2 0 0 1 0 4z"/></svg></span>
        <span class="contact-text">217 9th floor Harbour Line<br>Road NTB</span>
      </li>
      <li class="contact-item contact-item--phone">
        <span class="contact-icon"><svg viewBox="0 0 16 16" aria-hidden="true"><path d="M4.2 1.5l2.2 2.6-1.3 1.7c.9 1.9 2.3 3.3 4.2 4.2l1.7-1.3 2.6 2.2-1.2 2.4C7.2 13.1 2.9 8.8 1.8 3.6z"/></svg></span>
        <span class="contact-text">012 468 2579</span>
      </li>
      <li class="contact-item contact-item--email">
        <span class="contact-icon"><svg viewBox="0 0 16 16" aria-hidden="true"><path d="M1 3h14v10H1zm1.5 1.3v.4L8 8.6l5.5-3.9v-.4zm0 2.2v5.2h11V6.5L8 10.3z"/></svg></span>
        <span class="contact-text">yourname@cardmail.net</span>
      </li>
      <li class="contact-item contact-item--web">
        <span class="contact-icon"><svg viewBox="0 0 16 16" aria-hidden="true"><path d="M8 1a7 7 0 1 0 0 14A7 7 0 0 0 8 1zm0 1.3c.8.9 1.4 2.2 1.6 3.9H6.4C6.6 4.5 7.2 3.2 8 2.3zM2.4 7.4h2.8c0 .4 0 .8.1 1.2H2.4a5.6 5.6 0 0 1 0-1.2zm4 0h3.2v1.2H6.4zm4.4 0h2.8a5.6 5.6 0 0 1 0 1.2h-2.8v-1.2zM6.4 9.8h3.2c-.2 1.7-.8 3-1.6 3.9-.8-.9-1.4-2.2-1.6-3.9zM2.7 6.2a5.7 5.7 0 0 1 3-3.4 8 8 0 0 0-1.1 3.4zm7.7 0a8 8 0 0 0-1.1-3.4 5.7 5.7 0 0 1 3 3.4zM2.7 9.8h1.9a8 8 0 0 0 1.1 3.4 5.7 5.7 0 0 1-3-3.4zm7.7 0h1.9a5.7 5.7 0 0 1-3 3.4 8 8 0 0 0 1.1-3.4z"/></svg></span>
        <span class="contact-text">www.yoursitename.net</span>
      </li>
    </ul>

    <div class="brand">
      <span class="brand-mark"></span>
      <span class="brand-name">Drive Keystone</span>
    </div>
  </section>

  <section class="card card--back" aria-label="Business card back">
    <div class="back-face"></div>
  </section>
</main>
</body>
</html>
```